A4 Flyer Design outlining our financial philosophy

One A4 page design (landscape orientation) outlining our financial philosophy.
The design needs to show these steps as the building blocks and the path taken to financial success:
1. Maximise income and reduce expenses
2. Maximise savings and reduce bad debts
3. Invest wisely & tax effectively
4. Manage risk
5. Plan for retirement
6. Leave a legacy
The design needs to incorporate the 6 building blocks above along with the key points for each topic. More info attached.
Design must be engaging, professional and consistent with our current branding colours.

Target Market(s)

self employed individuals looking to build wealth through property and shares.

Industry/Entity Type

Financial Planning

Font styles to use
Sans Serif

Colors
0255a3
5c5c5c
000000
ffffff

Requirements
Must have
• clear and engaging.
• consistent with current branding
• 6 topics with key considerations (as per attached)
• must show that all 6 points are linked and are a journey.

```html
<!DOCTYPE html>
<html lang="en">
<head>
<meta charset="utf-8">
<title>Our Financial Philosophy</title>
<link rel="stylesheet" href="https://fonts.googleapis.com/css2?family=Roboto+Condensed:wght@300;400;700&family=Roboto+Slab:wght@800&display=swap">
<style>
  :root {
    --brand-blue: #0255a3;
    --deep-blue: #0a3f86;
    --navy: #062b5e;
    --slate: #5c5c5c;
    --charcoal: #3a3f47;
    --black: #000000;
    --white: #ffffff;
    --sky: #5fa8e6;
  }
  * { box-sizing: border-box; margin: 0; padding: 0; }
  html, body { width: 1200px; height: 800px; overflow: hidden; background: var(--white); }
  .flyer {
    position: relative; width: 1200px; height: 800px; overflow: hidden;
    font-family: "Roboto Condensed", "Arial Narrow", sans-serif; color: var(--white);
  }
  .backdrop {
    position: absolute; left: 0; top: 0; width: 1200px; height: 640px;
    background:
      radial-gradient(ellipse at 30% 35%, #bfe0fb 0%, rgba(150,200,245,0.6) 25%, transparent 55%),
      radial-gradient(ellipse at 80% 30%, #a9d3f7 0%, transparent 45%),
      linear-gradient(180deg, #2a78c8 0%, #5aa5e6 40%, #3d8bd6 75%, #1d63b4 100%);
  }
  .journey { position: absolute; left: 0; top: 0; }
  .step { position: absolute; width: 112px; text-align: center; }
  .step-number { font-size: 60px; font-weight: 700; line-height: 1; text-shadow: 0 2px 4px rgba(0,0,0,0.35); }
  .step-rule { width: 78px; height: 2px; background: var(--white); margin: 6px auto 8px; }
  .step-title { font-size: 15px; font-weight: 700; line-height: 1.22; text-transform: uppercase; }
  .step-title.light { font-weight: 400; }
  .points { list-style: none; text-align: left; margin-top: 10px; font-size: 10.5px; line-height: 1.25; font-weight: 400; }
  .points li { position: relative; padding-left: 11px; margin-bottom: 5px; }
  .points li::before { content: ""; position: absolute; left: 0; top: 3px; width: 7px; height: 7px; background: var(--white); }
  .success {
    position: absolute; left: 920px; top: 508px; width: 110px; height: 110px; border-radius: 50%;
    background: var(--deep-blue); display: flex; flex-direction: column; align-items: center; justify-content: center;
    text-align: center; font-size: 14px; font-weight: 700; line-height: 1.2; text-transform: uppercase;
  }
  .success .equals { font-size: 20px; line-height: 1; margin-bottom: 2px; }
  .footer { position: absolute; left: 0; top: 640px; width: 1200px; height: 160px; background: var(--white); }
  .footer-title {
    position: absolute; left: 250px; top: 58px; font-family: "Roboto Slab", Georgia, serif;
    font-weight: 800; font-size: 36px; color: var(--slate); letter-spacing: 0.5px;
  }
  .brand { position: absolute; right: 60px; top: 58px; display: flex; align-items: center; gap: 10px; }
  .brand-dot { width: 40px; height: 40px; border-radius: 50%; background: var(--brand-blue); }
  .brand-name { color: var(--brand-blue); font-weight: 700; font-size: 18px; line-height: 1.05; text-transform: uppercase; }
</style>
</head>
<body>
<div class="flyer">
  <div class="backdrop" role="img" aria-label="Blue-toned photograph of financial charts and data screens"></div>

  <svg class="journey" width="1200" height="640" viewBox="0 0 1200 640" aria-hidden="true">
    <defs>
      <linearGradient id="riseGrey" x1="0" y1="1" x2="0" y2="0">
        <stop offset="0" stop-color="#2c3138"/>
        <stop offset="1" stop-color="#5c5c5c"/>
      </linearGradient>
      <linearGradient id="riseFade" x1="0" y1="1" x2="0" y2="0">
        <stop offset="0" stop-color="#0a3f86" stop-opacity="0"/>
        <stop offset="0.55" stop-color="#3a3f47" stop-opacity="0.7"/>
        <stop offset="1" stop-color="#5c5c5c"/>
      </linearGradient>
    </defs>
    <!-- continuous path -->
    <path d="M150 600 L150 200 A82.5 82.5 0 0 1 315 200 L315 460 A82.5 82.5 0 0 0 480 460 L480 200 A82.5 82.5 0 0 1 645 200 L645 460 A82.5 82.5 0 0 0 810 460 L810 200 A82.5 82.5 0 0 1 975 200 L975 440"
          fill="none" stroke="#0255a3" stroke-width="112" stroke-opacity="0.92"/>
    <!-- step 1 rising arrow -->
    <path d="M100 600 L100 300 L62 300 L150 225 L238 300 L200 300 L200 600 Z" fill="url(#riseGrey)"/>
    <!-- step 3 and 5 rising heads -->
    <path d="M430 520 L430 300 L392 300 L480 225 L568 300 L530 300 L530 520 Z" fill="url(#riseFade)"/>
    <path d="M760 520 L760 300 L722 300 L810 225 L898 300 L860 300 L860 520 Z" fill="url(#riseFade)"/>
    <!-- descending heads -->
    <path d="M230 440 L400 440 L315 515 Z" fill="#062b5e" fill-opacity="0.85"/>
    <path d="M560 440 L730 440 L645 515 Z" fill="#062b5e" fill-opacity="0.85"/>
    <path d="M890 425 L1060 425 L975 500 Z" fill="#0255a3"/>
  </svg>

  <div class="step" style="left:94px; top:262px;">
    <div class="step-number">1</div>
    <div class="step-rule"></div>
    <div class="step-title">Maximise<br>Income<br>+<br>Reduce<br>Expenses</div>
    <ul class="points">
      <li>Invest in yourself through education and training</li>
      <li>Build a number of income streams</li>
      <li>Align your spending with your values</li>
      <li>Track your spending</li>
      <li>Increase surplus income</li>
    </ul>
  </div>

  <div class="step" style="left:259px; top:178px;">
    <div class="step-number">2</div>
    <div class="step-rule"></div>
    <div class="step-title">Maximise<br>Savings/<br>Equity<br>+<br>Reduce Bad<br>Expenses<br>Debts</div>
    <ul class="points">
      <li>Surplus income increases savings</li>
      <li>Use savings and equity for investment</li>
      <li>Avoid borrowing for lifestyle assets/ experiences where possible</li>
    </ul>
  </div>

  <div class="step" style="left:424px; top:262px;">
    <div class="step-number">3</div>
    <div class="step-rule"></div>
    <div class="step-title">Maximise<br>Income<br>+<br>Reduce<br>Expenses</div>
    <ul class="points">
      <li>Build an investment portfolio e.g. property and shares</li>
      <li>Use appropriate tax structures such as Family Trusts/ Superannuation</li>
      <li>Depreciation schedules</li>
    </ul>
  </div>

  <div class="step" style="left:589px; top:178px;">
    <div class="step-number">4</div>
    <div class="step-rule"></div>
    <div class="step-title">Invest<br>Wisely<br>&amp; Tax<br>Effectively</div>
    <ul class="points">
      <li>Insurance in various forms</li>
      <li>Contingency plans</li>
      <li>Diversification</li>
      <li>Focus on quality</li>
    </ul>
  </div>

  <div class="step" style="left:754px; top:262px;">
    <div class="step-number">5</div>
    <div class="step-rule"></div>
    <div class="step-title light">Manage<br>Risk</div>
    <ul class="points">
      <li>Replacement of your salary or profits from running a business with income from your investment portfolio</li>
      <li>Drawing a sustainable income to maintain a great lifestyle and protect your retirement nest egg</li>
    </ul>
  </div>

  <div class="step" style="left:919px; top:178px;">
    <div class="step-number">6</div>
    <div class="step-rule"></div>
    <div class="step-title light">Leave a<br>Legacy</div>
    <ul class="points">
      <li>Having a Will</li>
      <li>Power of Attorney</li>
      <li>Testamentary Trust?</li>
    </ul>
  </div>

  <div class="success">
    <span class="equals">=</span>
    <span>Financial<br>Success</span>
  </div>

  <footer class="footer">
    <h1 class="footer-title">OUR FINANCIAL PHILOSOPHY</h1>
    <div class="brand">
      <span class="brand-dot"></span>
      <span class="brand-name">Meridian<br>Financial Group</span>
    </div>
  </footer>
</div>
</body>
</html>
```